Business card for different employees

A professional new updated design incorporating our current business's color themes and styles such as our on-site service trucks decals included in pictures attached. Our current business card is very simple and not professionally designed. We are a small family business but want a professional corporate look.

Target Market(s)

Cards to be handed out to new customers , corperate meetings. For our on site service operators.

Industry/Entity Type

Hydraulic

Contact Information for Business Card

Address, website, phone number, email, logo.
slogan - "Industry chosen hose and fittings provider".
24/7 on-site service , supply and hose management
Experienced , indpendant , family owned

Font styles to use
Sans Serif

Requirements
Must have
• Easily editable so that I can add different names and different roles for employees etc.
Nice to have
• Freedom with colour doesn't necessarily have to be blue but that is our company colour theme with trucks and logo so makes sense for the card to have blue like the trucks.

```html
<!DOCTYPE html>
<html lang="en">
<head>
<meta charset="utf-8">
<title>Meridian Hose &amp; Fittings – Business Card</title>
<link rel="stylesheet" href="https://fonts.googleapis.com/css2?family=Lato:wght@400;700;900&display=swap">
<style>
  :root {
    --brand-blue: #3246a0;
    --brand-blue-deep: #2a3b8a;
    --ink: #111111;
    --paper: #ffffff;
    --backdrop: #d3e6ec;
    --decor: rgba(40, 50, 110, 0.45);
  }
  * { box-sizing: border-box; margin: 0; padding: 0; }
  html, body { width: 1200px; height: 900px; overflow: hidden; }
  body {
    background: var(--backdrop);
    font-family: "Lato", Arial, sans-serif;
    position: relative;
  }
  .card {
    position: absolute;
    width: 700px;
    height: 400px;
    border-radius: 22px;
    overflow: hidden;
  }
  .card--front { left: 250px; top: 30px; background: var(--paper); }
  .card--back  { left: 250px; top: 470px; background: var(--brand-blue); }

  /* Brand lockup */
  .brand { position: absolute; display: flex; align-items: center; gap: 14px; }
  .brand__mark {
    width: 62px; height: 62px; border-radius: 50%;
    background: var(--ink); flex: none;
  }
  .brand__name {
    font-weight: 900; font-size: 30px; letter-spacing: 1px;
    text-transform: uppercase; line-height: 1.05;
  }
  .brand__slogan {
    font-size: 12px; font-weight: 700; letter-spacing: .5px;
    text-transform: uppercase; margin-top: 6px;
  }
  .card--front .brand { left: 40px; top: 40px; }
  .card--front .brand__name { color: var(--brand-blue); }
  .card--front .brand__slogan { color: var(--brand-blue); }

  /* Front band */
  .rule { position: absolute; left: 0; right: 0; height: 3px; background: var(--ink); }
  .rule--top { top: 184px; }
  .rule--bottom { top: 340px; }
  .band {
    position: absolute; left: 0; right: 0; top: 192px; height: 142px;
    background: var(--brand-blue);
  }
  .band__mark {
    position: absolute; right: 40px; top: 22px;
    width: 76px; height: 76px; border-radius: 50%;
    background: var(--paper); border: 12px solid var(--ink);
  }
  .service-line {
    position: absolute; left: 40px; top: 148px;
    color: var(--brand-blue); font-weight: 700; font-size: 19px;
  }
  .contact { position: absolute; left: 40px; top: 214px; list-style: none; }
  .contact__item {
    display: flex; align-items: center; gap: 12px;
    color: var(--paper); font-size: 19px; line-height: 32px;
  }
  .contact__icon { width: 18px; height: 18px; flex: none; }
  .address {
    position: absolute; left: 40px; top: 356px;
    color: var(--ink); font-size: 17px;
  }

  /* Back */
  .decor-circle {
    position: absolute; right: -90px; top: -60px;
    width: 380px; height: 380px; border-radius: 50%;
    background: var(--decor);
  }
  .slot { position: absolute; width: 12px; height: 110px; background: var(--ink); border-radius: 6px; }
  .slot--left { left: 26px; top: 200px; }
  .slot--right { right: 26px; top: 60px; }
  .card--back .brand { left: 110px; top: 140px; }
  .card--back .brand__mark { width: 90px; height: 90px; }
  .card--back .brand__name { color: var(--paper); font-size: 38px; }
  .card--back .brand__slogan { color: var(--paper); font-size: 14px; }
  .values {
    position: absolute; left: 0; right: 0; top: 300px;
    text-align: center; color: var(--paper); font-size: 20px; font-weight: 700;
  }
  .values__dot {
    display: inline-block; width: 10px; height: 10px; border-radius: 50%;
    background: var(--paper); margin: 0 12px; vertical-align: middle;
  }
</style>
</head>
<body>

<section class="card card--front" aria-label="Card front">
  <div class="brand">
    <span class="brand__mark"></span>
    <div>
      <div class="brand__name">Meridian Hose &amp; Fittings</div>
      <div class="brand__slogan">Industry chosen hose and fittings provider</div>
    </div>
  </div>

  <p class="service-line">24/7 on-site service , supply and hose management</p>

  <div class="rule rule--top"></div>
  <div class="band">
    <span class="band__mark"></span>
  </div>
  <div class="rule rule--bottom"></div>

  <ul class="contact">
    <li class="contact__item">
      <svg class="contact__icon" viewBox="0 0 24 24" aria-hidden="true"><path fill="#fff" d="M6.6 10.8a15.1 15.1 0 0 0 6.6 6.6l2.2-2.2c.3-.3.7-.4 1-.2 1.1.4 2.3.6 3.6.6.6 0 1 .4 1 1V20c0 .6-.4 1-1 1A17 17 0 0 1 3 4c0-.6.4-1 1-1h3.5c.6 0 1 .4 1 1 0 1.3.2 2.5.6 3.6.1.3 0 .7-.2 1z"/></svg>
      0400 123 456
    </li>
    <li class="contact__item">
      <svg class="contact__icon" viewBox="0 0 24 24" aria-hidden="true"><path fill="#fff" d="M2 5h20v14H2zm2 2v.5l8 5 8-5V7l-8 5z"/></svg>
      contact@meridianhose.com
    </li>
    <li class="contact__item">
      <svg class="contact__icon" viewBox="0 0 24 24" aria-hidden="true"><circle cx="12" cy="12" r="9" fill="none" stroke="#fff" stroke-width="2"/><path d="M3 12h18M12 3c3 3 3 15 0 18M12 3c-3 3-3 15 0 18" fill="none" stroke="#fff" stroke-width="1.5"/></svg>
      www.meridianhose.com
    </li>
  </ul>

  <p class="address">88 Harbour Line Road, Unit 4, Westfield, ab 10001</p>
</section>

<section class="card card--back" aria-label="Card back">
  <span class="decor-circle"></span>
  <span class="slot slot--left"></span>
  <span class="slot slot--right"></span>
  <div class="brand">
    <span class="brand__mark"></span>
    <div>
      <div class="brand__name">Meridian Hose &amp; Fittings</div>
      <div class="brand__slogan">Industry chosen hose and fittings provider</div>
    </div>
  </div>
  <p class="values">Experienced<span class="values__dot"></span>indpendant<span class="values__dot"></span>family owned</p>
</section>

</body>
</html>
```